Integrated Health Clinic brochure

We need a brochure designed to highlight the services that we offer at the integrated clinic. Please see "Our Services" of our website for description of services to be added to the brochure except for Acupuncture, which is described below:

"Acupuncture is an ancient Chinese methodology that has been proven to be very effective in many health issues, particularly in relieving pain. It involves the stimulation of acupuncture points on the body to regain the natural balance of the body. Medical Acupuncture is effective in treating a wide variety of conditions including: headaches, neck and back pains, carpal tunnel syndrome, fibromyalgia, asthma, allergies, sinus problems, digestive disorders and many others."

our motto "Relieve, Rejuvenate, Renew"

Services we provide:
Chiropractic
Physiotherapy
Family counselling
Massage Therapy
Acupuncture
Osteopath

Colors are blue and green.

See our website www.solvarahealth.ca

```html
<!DOCTYPE html>
<html lang="en">
<head>
<meta charset="utf-8">
<title>Solvara Health Wellness – Services Brochure</title>
<link href="https://fonts.googleapis.com/css2?family=Arimo:wght@400;700&family=Roboto+Condensed:wght@400&display=swap" rel="stylesheet">
<style>
  :root {
    --blue: #41a6e8;
    --green: #86d12f;
    --slate: #55595d;
    --ink: #2a2a2a;
    --headline: #5b6064;
    --magenta: #e4269b;
    --paper: #ffffff;
  }
  * { margin: 0; padding: 0; box-sizing: border-box; }
  html, body { width: 928px; height: 1200px; overflow: hidden; background: var(--paper); }
  .brochure {
    position: relative; width: 928px; height: 1200px; overflow: hidden;
    font-family: "Arimo", Arial, sans-serif; color: var(--ink);
  }
  .service { position: absolute; width: 256px; }
  .service-tab {
    height: 33px; border-radius: 9px 9px 0 0;
    color: #fff; text-align: center;
    font-size: 17.5px; line-height: 34px; letter-spacing: 0.2px;
  }
  .tab-blue { background: var(--blue); }
  .tab-green { background: var(--green); }
  .tab-slate { background: var(--slate); }
  .service-body {
    margin-top: 15px; font-size: 13px; line-height: 18.1px;
    text-align: justify; hyphens: none;
  }
  .service-body strong { font-weight: 700; text-transform: uppercase; }
  .benefits { list-style: none; margin: 18px 0 10px; text-align: left; }
  .benefits li { position: relative; padding-left: 22px; margin-bottom: 4.5px; }
  .benefits li::before { content: "o"; position: absolute; left: 2px; top: 0; }
  .chiropractic { left: 43px; top: 43px; }
  .osteopathy { left: 43px; top: 420px; }
  .physiotherapy { left: 337px; top: 45px; }
  .massage { left: 337px; top: 310px; }
  .acupuncture { left: 630px; top: 43px; }
  .counselling { left: 630px; top: 326px; }

  .photo {
    position: absolute; border-radius: 50%;
    border: 3px solid #fff;
    box-shadow: 0 3px 10px rgba(0,0,0,0.22);
  }
  .photo-cartwheel { left: 95px; top: 710px; width: 218px; height: 218px;
    background: radial-gradient(circle at 45% 35%, #d9ecf8 0%, #9cc8ea 55%, #6fa94a 88%); }
  .photo-smile { left: 243px; top: 878px; width: 185px; height: 185px;
    background: radial-gradient(circle at 45% 45%, #f0c9a8 0%, #e8506a 45%, #5e9a2c 85%); }
  .photo-climb { left: 35px; top: 920px; width: 212px; height: 212px;
    background: linear-gradient(180deg, #e8eef4 0%, #b7c7d6 55%, #7a6a52 100%); }

  .motto {
    position: absolute; left: 633px; top: 620px;
    font-family: "Roboto Condensed", "Arial Narrow", sans-serif;
    color: var(--headline); line-height: 1;
  }
  .motto .big { display: block; font-size: 64px; height: 63px; letter-spacing: -0.5px; }
  .motto .small { font-size: 40px; }
  .motto .tail { display: block; font-size: 40px; margin-top: 10px; }

  .contact { position: absolute; left: 634px; top: 1008px; font-size: 17px; line-height: 21px; }
  .contact .clinic-name { color: var(--magenta); font-size: 21.5px; line-height: 28px; margin-bottom: 5px; }
  .contact .strong { font-weight: 700; }

  .footer-band { position: absolute; left: 0; top: 1152px; width: 928px; height: 48px; display: flex; }
  .footer-band .band-blue { width: 632px; background: var(--blue); }
  .footer-band .band-green { flex: 1; background: var(--green); }
</style>
</head>
<body>
<main class="brochure">

  <section class="service chiropractic">
    <h2 class="service-tab tab-blue">CHIROPRACTIC</h2>
    <p class="service-body"><strong>Chiropractic</strong> care is a safe, non-invasive, drug-free therapy to correct and prevent joint and muscle pain. By restoring the natural alignment in your body, chiropractic treatments restore movement and prevent potential injuries. Chiropractic treatments are especially effective in treating back, neck, pelvis and joint problems. Procedures most often used are adjustments or spinal manipulative therapy. Adjustments are safe, painless manual procedures where our skilled chiropractors manually apply pressures to your body to restore the natural alignment. Other treatments include various soft tissue techniques, Fascia Glide Technique, Kinesotaping, Ultrasound among others. Book an appointment now.</p>
  </section>

  <section class="service osteopathy">
    <h2 class="service-tab tab-blue">OSTEOPATHIC MEDICINE</h2>
    <p class="service-body"><strong>Osteopathic Medicine</strong> offers hands-on diagnosis and treatment through a system of therapy known as osteopathic manipulative medicine which emphases to promote the body’s innate ability to heal itself. Many of osteopathic techniques are aimed at reducing or eliminating the impediments to property structure and function so the self-healing mechanism of our bodies can assume its roles in restoring a person to health.</p>
  </section>

  <section class="service physiotherapy">
    <h2 class="service-tab tab-green">PHYSIOTHERAPY</h2>
    <p class="service-body"><strong>Physiotherapy</strong> is most well known for its ability to speed up the body’s recovery process from injury, illness or simple well and tear. Whether you are looking to get better from an injury or improve your body’s functionality, our physiotherapy treatments can get you back doing the things you love to do in improved performance. Some common treatments include ultrasound, manual therapy, electrical stimulation, physio-taping amongst others.</p>
  </section>

  <section class="service massage">
    <h2 class="service-tab tab-green">MASSAGE THEARPY</h2>
    <div class="service-body">
      <p><strong>Massage Thearpy</strong> is a mostly widely known for its relaxation and stress-release abilities, and it is also recognized as an effective treatment for treating illness and also as a tool in preventative medicine. Safe and effective massage treatments need to be carried out by a Registered Massage Therapist. Benefits of therapeutic massages include:</p>
      <ul class="benefits">
        <li>Treatment and elimination of chronic pain and acute conditions</li>
        <li>Relaxation and release stress</li>
        <li>Improve circulation</li>
        <li>Improve mobility and balance</li>
        <li>Improve the functioning of immune system</li>
        <li>Lymphatic drainage</li>
      </ul>
      <p>Whether you are looking to get rid of that sore back and leg or looking for improve your golf swing, therapeutic massages can help. Book an appointment now.</p>
    </div>
  </section>

  <section class="service acupuncture">
    <h2 class="service-tab tab-slate">ACUPUNCTURE</h2>
    <p class="service-body"><strong>Acupuncture</strong> is an ancient Chinese methodology that has been proven to be very effective in many health issues, particularly in relieving pain. It involves the stimulation of acupuncture points on the body to regain the natural balance of the body. Medical Acupuncture is effective in treating a wide variety of conditions including: headaches, neck and back pains, carpal tunnel syndrome, fibromyalgia, asthma, allergies, sinus problems, digestive disorders and many others.</p>
  </section>

  <section class="service counselling">
    <h2 class="service-tab tab-slate">FAMILY COUNSELLING</h2>
    <p class="service-body">Our relationships with ourselves and our loved ones is an integrated part of our overall well being and can often influence our bodies physically. Our registered Social Work practitioner assists clients in handling individual, family, emotional or educational issues in a professional and confidential manner. Whether it is marital issues, parenting concerns or individ1al matters, a chat with our counsellor can ease your stress and put you on the right path.</p>
  </section>

  <div class="photo photo-cartwheel" role="img" aria-label="Photo of a woman doing a cartwheel on grass under a blue sky"></div>
  <div class="photo photo-climb" role="img" aria-label="Photo of two climbers raising joined hands on a rocky summit"></div>
  <div class="photo photo-smile" role="img" aria-label="Photo of a smiling young woman with a braid lying on grass"></div>

  <h1 class="motto">
    <span class="big">PAIN <span class="small">is</span></span>
    <span class="big">NOT <span class="small">a</span></span>
    <span class="big">NORMAL</span>
    <span class="big">PART</span>
    <span class="tail">of life!</span>
  </h1>

  <address class="contact" style="font-style:normal">
    <p class="clinic-name">Solvara Health Wellness</p>
    <p>1480 Maple Street, Suite 310</p>
    <p>Toronto, Ontario</p>
    <p class="strong" style="margin-top:4px">1-866-555-0142</p>
    <p class="strong">www.solvarahealth.ca</p>
  </address>

  <div class="footer-band"><span class="band-blue"></span><span class="band-green"></span></div>
</main>
</body>
</html>
```